MossVane Spa, Skincare and Cosmetics website

I need a website for MossVane (putting the glow back into people's skin) which allows viewers to access information about Beauty Spa packaging and facilities as well as online skincare and cosmetic products. Our distinctive difference is that our products are certified organic. We want to target a luxury high income niche market (age 30-50). I want all colours to be "baby colours" preferably background to be "baby metallic pink" (but please don't make the website too immature) with curves as patterns. I want a romantic vintage look.

The website needs to look:
1. elegant (prestige and luxury)
2. bright (baby colours mainly)
3. European curves and signature patterns
4. Can include Pearl related pics (but not a must)

The website pages needs to have:
1. pages ordering skincare/cosmetics
2. shopping cart and payment
3. about us and about our product differences
4. contact us
5. booking for spa treatments and packages

I have attached our logo and also packaging label styles.

Industry/Entity Type

Cosmetics

```html
<!DOCTYPE html>
<html lang="en">
<head>
<meta charset="utf-8">
<title>MossVane Spa, Skincare and Cosmetics</title>
<link href="https://fonts.googleapis.com/css2?family=Cinzel:wght@400;600&family=Pacifico&family=Open+Sans:wght@400;600&display=swap" rel="stylesheet">
<style>
  :root{
    --rose:#e9467a;
    --rose-soft:#f4a3b7;
    --blush-bg:#fbe9ef;
    --panel:#f5ecea;
    --panel-line:#dcbcb3;
    --taupe:#c9a198;
    --moss:#6cbf4a;
    --moss-dark:#4f9a33;
    --sky:#7aaee0;
    --ink:#1f1f1f;
    --sand-a:#d9c4a2;
    --sand-b:#a88d68;
    --footer:#333333;
    --white:#ffffff;
  }
  *{box-sizing:border-box;margin:0;padding:0}
  html,body{width:1200px;height:900px;overflow:hidden}
  body{position:relative;font-family:"Open Sans",sans-serif;background:var(--blush-bg)}
  .abs{position:absolute}

  .backdrop{left:0;top:44px;width:1200px;height:814px;
    background:linear-gradient(180deg,#fde9f0 0%,#fbe3ec 55%,var(--sand-a) 64%,var(--sand-b) 100%)}

  .topbar{left:0;top:0;width:1200px;height:44px;background:var(--rose);box-shadow:0 2px 4px rgba(0,0,0,.15)}
  .social{left:224px;top:9px;display:flex;gap:12px}
  .social span{width:26px;height:26px;background:var(--white);border-radius:3px;display:block}
  .account{right:306px;top:13px;color:var(--white);font-family:"Cinzel",serif;font-size:12px;white-space:nowrap}
  .cart{left:900px;top:4px;color:var(--white);font-family:"Pacifico",cursive;font-size:22px;display:flex;align-items:center;gap:6px;white-space:nowrap}

  .frame{left:0;top:0}

  .brand{left:400px;top:110px;width:400px;text-align:center}
  .brand .dot{width:46px;height:46px;border-radius:50%;background:var(--taupe);margin:0 auto 6px;opacity:.8}
  .brand .name{font-family:"Cinzel",serif;font-size:30px;color:var(--taupe);letter-spacing:1px}

  .ribbon{left:160px;top:206px}
  .nav{left:222px;top:210px;height:44px;display:flex;align-items:center;font-family:"Cinzel",serif;font-size:14px;color:var(--white);white-space:nowrap}
  .nav a{color:var(--white);text-decoration:none;padding:0 12px;height:44px;line-height:44px;display:block}
  .nav a.active{background:var(--rose)}

  .slider{left:234px;top:254px;width:732px;height:204px;
    background:linear-gradient(90deg,#f1ddd3 0%,#fbf3ef 30%,#ffffff 50%,#f3e3d2 75%,#e7d2bd 100%)}
  .arrow{top:322px;width:37px;height:56px;background:#9d9d9d;color:var(--white);font-size:32px;line-height:52px;text-align:center;font-family:"Open Sans",sans-serif}
  .arrow.prev{left:234px}
  .arrow.next{left:929px}

  .welcome{left:234px;top:460px;width:732px;height:32px;background:#efe4e1;text-align:center;
    font-family:"Cinzel",serif;font-size:24px;line-height:32px;color:#d2b3aa;letter-spacing:1px}

  .col-title{top:504px;font-family:"Pacifico",cursive;font-size:20px;font-weight:400;white-space:nowrap}
  .t-believe{left:246px;color:var(--rose)}
  .t-featured{left:516px;color:var(--moss)}
  .t-visit{left:768px;color:var(--sky)}

  .believe-text{left:246px;top:540px;width:228px;font-size:10px;line-height:13px;color:var(--ink)}
  .believe-text p+p{margin-top:13px}

  .tile{top:534px;width:230px;height:124px;border:1px solid #d8d0cc;background:var(--white);padding:5px}
  .tile .fill{width:100%;height:100%}
  .featured{left:486px}
  .featured .fill{background:linear-gradient(135deg,#f2f2f2,#e9e2d8 50%,#fafafa)}
  .badge{right:5px;top:5px;width:70px;height:70px;overflow:hidden}
  .badge span{position:absolute;right:-26px;top:18px;width:110px;transform:rotate(45deg);background:var(--rose-soft);color:var(--white);font-family:"Pacifico",cursive;font-size:12px;text-align:center;line-height:20px}
  .visit{left:724px}
  .visit .fill{background:linear-gradient(135deg,#eef0e6,#e4e6d8)}

  .cta{top:666px;width:230px;height:49px;color:var(--white);font-family:"Pacifico",cursive;font-size:24px;text-align:center;line-height:46px;white-space:nowrap}
  .cta.packages{left:246px;background:var(--rose-soft)}
  .cta.spa{left:486px;background:var(--moss)}
  .cta.sellers{left:724px;background:var(--sky)}

  .divider{left:246px;top:727px;width:708px;border-top:1px dashed var(--panel-line)}

  .sign{left:400px;top:740px;width:400px;text-align:center}
  .sign .name{font-family:"Cinzel",serif;font-size:24px;color:#c7aaa2;letter-spacing:1px}
  .sign .phone{font-family:"Cinzel",serif;font-size:20px;color:var(--rose);margin-top:2px}

  .footer{left:0;top:858px;width:1200px;height:42px;background:var(--footer);color:var(--white);
    font-family:"Cinzel",serif;font-size:12px;display:flex;align-items:center;padding-left:247px;white-space:nowrap}
  .footer .links{margin-left:16px}
</style>
</head>
<body>
  <div class="abs backdrop" role="img" aria-label="Soft pink curved chevron pattern above a sandy beach with two pearls"></div>

  <header class="abs topbar">
    <div class="abs social"><span></span><span></span></div>
    <div class="abs account">Login/Register | View Order Status |</div>
    <div class="abs cart">Cart
      <svg width="26" height="22" viewBox="0 0 26 22"><path d="M1 2h4l3 12h13l3-9H7" fill="none" stroke="#fff" stroke-width="2.4" stroke-linejoin="round"/><rect x="8" y="5" width="15" height="9" fill="#fff"/><circle cx="10" cy="19" r="2" fill="#fff"/><circle cx="20" cy="19" r="2" fill="#fff"/></svg>
    </div>
  </header>

  <svg class="abs frame" width="1200" height="900" viewBox="0 0 1200 900">
    <path d="M236 150 H398 C418 150 414 112 448 100 C500 84 560 78 600 78 C640 78 700 84 752 100 C786 112 782 150 802 150 H964 Q976 150 976 162 V768 Q976 780 964 780 H802 C782 780 786 812 752 820 C700 830 640 832 600 832 C560 832 500 830 448 820 C414 812 418 780 398 780 H236 Q224 780 224 768 V162 Q224 150 236 150 Z" fill="#f5ecea" stroke="#dcbcb3" stroke-width="4"/>
    <path d="M244 160 H404 C424 160 424 124 454 112 C504 94 560 90 600 90 C640 90 696 94 746 112 C776 124 776 160 796 160 H956 Q966 160 966 170 V760 Q966 770 956 770 H796 C776 770 776 802 746 810 C696 820 640 822 600 822 C560 822 504 820 454 810 C424 802 424 770 404 770 H244 Q234 770 234 760 V170 Q234 160 244 160 Z" fill="none" stroke="#e4cdc6" stroke-width="1.5"/>
  </svg>

  <div class="abs brand">
    <div class="dot"></div>
    <div class="name">MossVane</div>
  </div>

  <svg class="abs ribbon" width="882" height="60" viewBox="0 0 882 60">
    <path d="M0 14 H40 V54 H0 L14 34 Z" fill="#4f9a33"/>
    <path d="M882 14 H842 V54 H882 L868 34 Z" fill="#4f9a33"/>
    <rect x="20" y="4" width="842" height="44" fill="#6cbf4a"/>
  </svg>
  <nav class="abs nav">
    <a class="active">Home</a><a>Makeup</a><a>Skincare</a><a>Gifts</a><a>Beauty Tips</a><a>About Us</a><a>Clearance</a><a>Offers</a><a>Contact Us</a>
  </nav>

  <div class="abs slider" role="img" aria-label="Slide showing a woman with radiant skin beside organic skincare jars and serum bottles"></div>
  <div class="abs arrow prev">&lt;</div>
  <div class="abs arrow next">&gt;</div>

  <div class="abs welcome">Welcome to MossVane</div>

  <h2 class="abs col-title t-believe">What we believe in</h2>
  <h2 class="abs col-title t-featured">Featured Product</h2>
  <h2 class="abs col-title t-visit">Come Visit Us !</h2>

  <div class="abs believe-text">
    <p>This particular section is to demonstrate what the welcome paragraph can look like. You can replace information in this area with anything you like, including, but not limited to, a mission statement or maybe even an “about us” section.</p>
    <p>This could be setup for a secondary paragraph if you have more than one paragraph worth of information.</p>
  </div>

  <div class="abs tile featured">
    <div class="fill" role="img" aria-label="Featured organic skincare product range"></div>
    <div class="abs badge"><span>New!</span></div>
  </div>
  <div class="abs tile visit">
    <div class="fill" role="img" aria-label="Street map showing the spa location"></div>
  </div>

  <div class="abs cta packages">Our Packages</div>
  <div class="abs cta spa">Spa Treatments</div>
  <div class="abs cta sellers">Top Sellers</div>

  <div class="abs divider"></div>

  <div class="abs sign">
    <div class="name">MossVane</div>
    <div class="phone">1-800-000-0000</div>
  </div>

  <footer class="abs footer">
    <span>Copyright © 2014 MossVane. All rights reserved.</span>
    <span class="links">Privacy Policy | Terms &amp; Conditions | About Us | FAQ | Sitemap</span>
  </footer>
</body>
</html>
```